Criação de Kit Layout de Posts para Redes Sociais (Facebook, Instagram e etc) para Tecnologia & Ciencias
A empresa queria:
" DESENVOLVE, IMPLANTA O SOFTWARE E DA SUPORTE (AO CLIENTE). "

```html
<!DOCTYPE html>
<html lang="pt-BR">
<head>
<meta charset="UTF-8">
<title>Nexora Software — Desenvolvimento, Implantação e Suporte</title>
<link rel="stylesheet" href="https://fonts.googleapis.com/css2?family=Montserrat:wght@500;600;700&family=Roboto:wght@400&display=swap">
<style>
  :root {
    --orange: #f08a1c;
    --white: #ffffff;
    --ink-deep: #1d2126;
    --ink-mid: #3a4048;
    --warm-light: #a59580;
    --vest: #8a8f3a;
  }
  html, body {
    margin: 0;
    padding: 0;
    width: 1200px;
    height: 1200px;
    overflow: hidden;
    background: var(--ink-deep);
  }
  .post {
    position: relative;
    width: 1200px;
    height: 1200px;
    overflow: hidden;
    font-family: "Montserrat", sans-serif;
    color: var(--white);
  }
  .scene-photo {
    position: absolute;
    inset: 0;
    background:
      radial-gradient(ellipse 35% 45% at 78% 45%, rgba(190,160,120,0.55), transparent 70%),
      radial-gradient(ellipse 30% 20% at 88% 28%, rgba(240,170,40,0.55), transparent 70%),
      radial-gradient(ellipse 20% 35% at 15% 75%, rgba(138,143,58,0.45), transparent 70%),
      linear-gradient(100deg, #2b2f35 0%, #4a4540 35%, #7d6f60 60%, #3a3a3c 100%);
  }
  .scene-shade {
    position: absolute;
    inset: 0;
    background:
      linear-gradient(90deg, rgba(20,22,26,0.75) 0%, rgba(20,22,26,0.3) 55%, rgba(20,22,26,0.1) 100%),
      linear-gradient(180deg, rgba(20,22,26,0) 60%, rgba(20,22,26,0.85) 100%);
  }
  .brand {
    position: absolute;
    left: 66px;
    top: 66px;
    display: flex;
    align-items: center;
    gap: 26px;
  }
  .brand-mark {
    width: 134px;
    height: 134px;
    border-radius: 50%;
    background: var(--orange);
  }
  .brand-name {
    font-weight: 700;
    font-size: 64px;
    letter-spacing: -1px;
    color: var(--white);
    white-space: nowrap;
  }
  .headline {
    position: absolute;
    left: 91px;
    top: 418px;
    margin: 0;
    font-weight: 600;
    font-size: 44px;
    line-height: 56px;
    letter-spacing: 0.5px;
    text-transform: uppercase;
  }
  .headline .accent {
    display: block;
    color: var(--orange);
    font-size: 62px;
    line-height: 72px;
  }
  .social {
    position: absolute;
    left: 103px;
    top: 1010px;
    display: flex;
    gap: 22px;
  }
  .social-dot {
    width: 46px;
    height: 46px;
    border-radius: 50%;
    background: var(--white);
  }
  .contacts {
    position: absolute;
    left: 101px;
    top: 1088px;
    width: 1060px;
    height: 70px;
    font-family: "Roboto", sans-serif;
    font-size: 16px;
    line-height: 20px;
  }
  .contact {
    position: absolute;
    top: 0;
    height: 60px;
    display: flex;
    align-items: center;
    gap: 20px;
    white-space: nowrap;
  }
  .contact-phone { left: 0; }
  .contact-web { left: 367px; }
  .contact-address { left: 768px; }
  .contact-icon {
    width: 54px;
    height: 54px;
    border-radius: 8px;
    background: var(--white);
    display: flex;
    align-items: center;
    justify-content: center;
    flex-shrink: 0;
  }
  .contact-icon svg { width: 34px; height: 34px; }
</style>
</head>
<body>
<main class="post">
  <div class="scene-photo" role="img" aria-label="Foto de fundo: profissional com capacete amarelo e colete refletivo olhando para as prateleiras de um depósito, segurando um tablet, com colegas desfocados ao fundo"></div>
  <div class="scene-shade"></div>

  <header class="brand">
    <div class="brand-mark"></div>
    <span class="brand-name">Nexora Software</span>
  </header>

  <h1 class="headline">
    Desenvolvimento,<br>
    Implantação<br>
    e suporte de
    <span class="accent">Software</span>
  </h1>

  <div class="social" aria-label="Redes sociais">
    <span class="social-dot"></span>
    <span class="social-dot"></span>
  </div>

  <footer class="contacts">
    <div class="contact contact-phone">
      <span class="contact-icon">
        <svg viewBox="0 0 24 24" aria-hidden="true">
          <path fill="#1d2126" d="M6.6 10.8a15.1 15.1 0 0 0 6.6 6.6l2.2-2.2c.3-.3.7-.4 1-.2 1.1.4 2.3.6 3.6.6.6 0 1 .4 1 1V20c0 .6-.4 1-1 1A17 17 0 0 1 3 4c0-.6.4-1 1-1h3.5c.6 0 1 .4 1 1 0 1.3.2 2.5.6 3.6.1.3 0 .7-.2 1z"/>
        </svg>
      </span>
      <span>+55 (21) 98765-4321<br>+55 (21) 3456-7890</span>
    </div>
    <div class="contact contact-web">
      <span class="contact-icon">
        <svg viewBox="0 0 24 24" aria-hidden="true" fill="none" stroke="#1d2126" stroke-width="1.8">
          <circle cx="12" cy="12" r="9"/>
          <ellipse cx="12" cy="12" rx="4" ry="9"/>
          <line x1="3" y1="12" x2="21" y2="12"/>
          <path d="M5 7h14M5 17h14"/>
        </svg>
      </span>
      <span>contato@nexorasoft.com.br<br>www.nexorasoft.com.br</span>
    </div>
    <div class="contact contact-address">
      <span class="contact-icon">
        <svg viewBox="0 0 24 24" aria-hidden="true">
          <path fill="#1d2126" d="M12 2a7 7 0 0 0-7 7c0 5.2 7 13 7 13s7-7.8 7-13a7 7 0 0 0-7-7zm0 9.5A2.5 2.5 0 1 1 12 6.5a2.5 2.5 0 0 1 0 5z"/>
        </svg>
      </span>
      <span>Rua das Acácias, 2450<br>Bairro Jardim Aurora<br>04567-120 - São Paulo / SP</span>
    </div>
  </footer>
</main>
</body>
</html>
```